New women's health clinic needs a new home!!

We need a professional website for our modern women's health clinic. Needs to be in wordpress. Back end needs to be accesible by novice admin staff. Text and stock photography supplied by us. We need approximately 5 pages with 3-4 subpages each. Links to social media a must. Blog a must. Patients will need to be able to download e-books after supplying an e-mail address. Mobile-friendly is a must!

We created our logo through this site. Please refer to the logo for style themes.

Target Market(s)

Women aged 28-55

Industry/Entity Type

Health

Coding

Coded - Design and coding required

Number of Pages Required

5+ page

Font styles to use
Sans Serif

Colors
886aae
cee9f5
3377b5
d3a5cc
ffffff
eddcec
6e479c
85abd2
876aae

Requirements
Must have
• Wordpress
• Social media ready
• Mobile-friendly to Plinexa's specs
• Ability to download e-books
• Captures data on back end

```html
<!DOCTYPE html>
<html lang="en">
<head>
<meta charset="utf-8">
<title>Meridian Women's Health</title>
<link href="https://fonts.googleapis.com/css2?family=Raleway:wght@400;500;600;700&family=Open+Sans:ital,wght@0,400;0,600;0,700;1,400&display=swap" rel="stylesheet">
<style>
:root{
  --ink:#2e2e2e;
  --body:#6a6a6a;
  --blue:#2f6fb3;
  --btn-blue:#0f5aa8;
  --pink:#dd86cc;
  --sky:#cfe8f4;
  --mauve:#ead9ea;
  --lilac:#886aae;
  --footer:#252525;
  --white:#ffffff;
  --orange:#f29a1e;
}
*{box-sizing:border-box;margin:0;padding:0}
html,body{width:1200px;height:2683px;overflow:hidden;background:var(--white)}
body{position:relative;font-family:"Open Sans",sans-serif;color:var(--body)}
.abs{position:absolute}

/* header */
.site-header{position:absolute;left:0;top:0;width:1200px;height:178px;background:var(--white)}
.brand-mark{left:143px;top:24px;width:86px;height:86px;border-radius:50%;background:var(--lilac)}
.brand-name{left:97px;top:120px;width:180px;text-align:center;font-family:"Raleway",sans-serif;font-weight:700;font-size:17px;line-height:20px;color:#1f1f1f;letter-spacing:.3px}
.ebook-btn{left:867px;top:63px;width:198px;height:66px;background:var(--btn-blue);border-radius:3px;display:flex;align-items:center;padding-left:22px;gap:20px;color:var(--white);font-family:"Raleway",sans-serif;font-weight:600;font-size:15px;line-height:21px;letter-spacing:.5px}

/* nav */
.main-nav{position:absolute;left:0;top:178px;width:1200px;height:58px;background:linear-gradient(#4a4a4a,#2b2b2b)}
.main-nav a{position:absolute;top:0;height:58px;line-height:58px;transform:translateX(-50%);color:var(--white);text-decoration:none;font-family:"Raleway",sans-serif;font-weight:700;font-size:12.5px;letter-spacing:.4px}
.main-nav a.active{left:97px;width:100px;transform:none;text-align:center;background:var(--pink)}

/* hero */
.hero{left:0;top:236px;width:1200px;height:607px}
.hero-photo{width:100%;height:100%;
  background:
    linear-gradient(180deg,rgba(255,255,255,.35) 0%,rgba(255,255,255,0) 40%),
    linear-gradient(90deg,#dfe8f0 0%,#e9d6c4 10%,#9fb0dc 17%,#8fa3d8 40%,#f0d8cc 50%,#e9dfe2 62%,#e7a9c3 75%,#f0b9cf 100%)}
.hero-arrow{top:283px;width:40px;height:40px;border-radius:50%;background:var(--orange);display:flex;align-items:center;justify-content:center;box-shadow:0 1px 3px rgba(0,0,0,.3)}
.hero-dots{left:560px;top:578px;display:flex;gap:6px}
.hero-dots span{width:8px;height:8px;border-radius:50%;background:#c8c8c8}
.hero-dots span:first-child{background:#2c4f8c}

/* welcome */
.welcome-photo{left:97px;top:930px;width:441px;height:297px;border:4px solid var(--white);box-shadow:0 0 4px rgba(0,0,0,.25);
  background:linear-gradient(90deg,#4b4f57 0%,#6a6c72 18%,#f1f0ee 30%,#f4f3f1 62%,#c9a98a 72%,#b08a62 100%)}
.welcome-title{left:572px;top:922px;font-family:"Raleway",sans-serif;font-weight:500;font-size:32px;color:var(--ink)}
.welcome-text{left:572px;top:984px;width:500px;font-size:13px;line-height:25px;color:var(--body)}
.learn-btn{left:572px;top:1169px;width:164px;height:52px;background:var(--pink);color:var(--white);font-family:"Raleway",sans-serif;font-size:18px;letter-spacing:.5px;display:flex;align-items:center;justify-content:center;border-radius:2px}

/* services */
.services{left:0;top:1282px;width:1200px;height:521px;background:var(--sky)}
.section-title{font-family:"Raleway",sans-serif;font-weight:500;color:var(--ink)}
.services .section-title{position:absolute;left:0;width:1200px;top:45px;text-align:center;font-size:35px}
.service-photo{width:209px;height:145px;border:3px solid var(--white)}
.service-name{font-family:"Raleway",sans-serif;font-weight:600;font-size:19px;color:var(--blue);letter-spacing:.3px}
.service-text{width:230px;font-size:13px;line-height:22.5px;color:var(--body)}
.read-more{font-size:13.5px;font-weight:600;color:#333}

/* testimonial */
.quote-badge{left:547px;top:1856px;width:68px;height:68px;border-radius:50%;border:2px solid #555;display:flex;align-items:center;justify-content:center}
.avatar{left:107px;top:1932px;width:125px;height:125px;border-radius:50%;border:5px solid #eee;background:linear-gradient(180deg,#f4f2f0 0%,#e4c7a8 45%,#d9b08a 100%);box-shadow:0 0 0 1px #ddd}
.quote-text{left:274px;top:1946px;width:800px;font-style:italic;font-size:13.3px;line-height:25px;color:#666}
.quote-open{left:253px;top:1930px;font-family:Georgia,serif;font-size:30px;color:#333}
.quote-author{left:274px;top:2046px;font-family:"Raleway",sans-serif;font-weight:700;font-size:16px;color:var(--blue)}
.quote-author small{font-family:"Open Sans",sans-serif;font-weight:400;font-size:12px;color:#999;margin-left:6px}

/* gallery */
.gallery{left:0;top:2121px;width:1200px;height:322px;background:var(--mauve)}
.gallery .section-title{position:absolute;left:97px;top:42px;font-size:31px}
.gallery-nav{left:1024px;top:70px;display:flex;gap:3px}
.gallery-nav span{width:19px;height:19px;background:#8a8a8a;display:flex;align-items:center;justify-content:center}
.gallery-item{top:101px;width:229px;height:170px;border:3px solid var(--white)}

/* footer */
.site-footer{left:0;top:2443px;width:1200px;height:240px;background:var(--footer);color:#bdbdbd}
.footer-title{font-family:"Raleway",sans-serif;font-weight:400;font-size:18px;color:var(--white)}
.footer-line{font-size:12.5px;line-height:22px;color:#b5b5b5;display:flex;gap:10px}
.social{display:flex;gap:4px}
.social span{width:38px;height:38px;border-radius:50%;background:var(--white);display:flex;align-items:center;justify-content:center}
.social span::after{content:"";width:18px;height:18px;border-radius:50%;background:var(--footer)}
.copyright{left:0;width:1200px;text-align:center;font-size:12.5px;color:#7d7d7d}
.copyright b{color:var(--white);font-weight:400}
</style>
</head>
<body>

<header class="site-header">
  <div class="abs brand-mark"></div>
  <div class="abs brand-name">MERIDIAN<br>WOMEN'S HEALTH</div>
  <a class="abs ebook-btn">
    <svg width="26" height="26" viewBox="0 0 26 26" fill="#fff"><path d="M10 2h6v10h5l-8 8-8-8h5z"/><rect x="2" y="21" width="22" height="4"/></svg>
    <span>DOWNLOAD<br>E-BOOK</span>
  </a>
</header>

<nav class="main-nav">
  <a class="active">HOME</a>
  <a style="left:247px">ABOUT</a>
  <a style="left:368px">PATIENTS</a>
  <a style="left:579px">AGENCIES/PHYSICIANS/CLIENTS</a>
  <a style="left:789px">THERAPISTS</a>
  <a style="left:894px">FAQ</a>
  <a style="left:996px">CONTACT</a>
</nav>

<section class="abs hero">
  <div class="hero-photo" role="img" aria-label="Physiotherapist in blue scrubs helping an older woman in pink lift a small hand weight"></div>
  <div class="abs hero-arrow" style="left:44px"><svg width="16" height="16" viewBox="0 0 16 16"><path d="M11 2 4 8l7 6z" fill="#8b1d10"/></svg></div>
  <div class="abs hero-arrow" style="left:1080px"><svg width="16" height="16" viewBox="0 0 16 16"><path d="M5 2l7 6-7 6z" fill="#8b1d10"/></svg></div>
  <div class="abs hero-dots"><span></span><span></span><span></span><span></span></div>
</section>

<section class="welcome">
  <div class="abs welcome-photo" role="img" aria-label="Smiling male therapist in a white shirt in a clinic"></div>
  <h1 class="abs welcome-title">Welcome to Our Website</h1>
  <p class="abs welcome-text">Praesent non dolor quis turpis placerat suscipit. Nunc quis velit magna. Lorem ipsum dolor sit amet, consectetur adipiscing elit. Vivamus et erat dolor. Vestibulum sollicitudin mollis ligula, dictum fringilla velit scelerisque a. Mauris ligula justo, mattis a pellentesque a, aliquam egestas magna. Donec fringilla velit sit amet quam tempus venenatis. Class aptent taciti sociosqu ad litora torquent per conubia nostra, per inceptos himenaeos.</p>
  <a class="abs learn-btn">LEARN MORE</a>
</section>

<section class="abs services">
  <h2 class="section-title">Our Services</h2>

  <div class="abs service-photo" style="left:97px;top:120px;background:linear-gradient(90deg,#eef0f2 0%,#c9c6c4 30%,#e9d7c2 55%,#7a7e86 85%,#3f4550 100%)" role="img" aria-label="Two older women smiling together"></div>
  <div class="abs" style="left:333px;top:120px">
    <h3 class="service-name">NEQUE PORRO</h3>
    <p class="service-text" style="margin-top:6px">Praesent non dolor quis turpis plac erat suscipit. Nunc quis velit magna. Lorem ipsum dolor elit.</p>
    <p class="read-more" style="margin-top:8px">Read More &gt;&gt;</p>
  </div>

  <div class="abs service-photo" style="left:594px;top:120px;background:linear-gradient(180deg,#dfe9f2 0%,#a9c3dc 35%,#c77fb0 65%,#b58cc4 80%,#e6d3c8 100%)" role="img" aria-label="Women stretching in a fitness class"></div>
  <div class="abs" style="left:828px;top:120px">
    <h3 class="service-name">QUISQUAM EST</h3>
    <p class="service-text" style="margin-top:6px">Praesent non dolor quis turpis plac erat suscipit. Nunc quis velit magna. Lorem ipsum dolor elit.</p>
    <p class="read-more" style="margin-top:8px">Read More &gt;&gt;</p>
  </div>

  <div class="abs service-photo" style="left:97px;top:318px;background:linear-gradient(90deg,#f4f1ee 0%,#e2c7ad 35%,#f6f3f0 60%,#c89a7c 85%,#6a4a3c 100%)" role="img" aria-label="Doctor consulting with a young patient"></div>
  <div class="abs" style="left:333px;top:318px">
    <h3 class="service-name">DOLOREM PUM</h3>
    <p class="service-text" style="margin-top:6px">Praesent non dolor quis turpis plac erat suscipit. Nunc quis velit magna. Lorem ipsum dolor elit.</p>
    <p class="read-more" style="margin-top:8px">Read More &gt;&gt;</p>
  </div>

  <div class="abs service-photo" style="left:594px;top:318px;background:linear-gradient(90deg,#d8d4cf 0%,#eeece9 35%,#f3eee8 60%,#e8c98a 80%,#dedad4 100%)" role="img" aria-label="Older woman relaxing with a drink"></div>
  <div class="abs" style="left:828px;top:318px">
    <h3 class="service-name">ADIPISCI VELIT</h3>
    <p class="service-text" style="margin-top:6px">Praesent non dolor quis turpis plac erat suscipit. Nunc quis velit magna. Lorem ipsum dolor elit.</p>
    <p class="read-more" style="margin-top:8px">Read More &gt;&gt;</p>
  </div>
</section>

<section class="testimonial">
  <div class="abs quote-badge"><svg width="24" height="20" viewBox="0 0 24 20" fill="#333"><path d="M0 10q0-9 9-10v4q-4 1-4 5h4v11H0zM13 10q0-9 9-10v4q-4 1-4 5h4v11h-9z"/></svg></div>
  <div class="abs avatar" role="img" aria-label="Portrait of a client"></div>
  <div class="abs quote-open">&ldquo;</div>
  <p class="abs quote-text">Praesent non dolor quis turpis placerat suscipit. Nunc quis velit magna. Lorem ipsum dolor sit amet, consectetur adipiscing elit. Vm dolor. Vestibulum sollicitudin mollis ligula, dictum fringilla velit scelerisque a. Mauris ligula justo, mattis a pellentesque a, aliquam magna. Donec fringilla velit sit amet quam tempus venenatis....</p>
  <p class="abs quote-author">Lena Harwick, <small>Newyork</small> <span style="font-family:Georgia,serif;font-size:24px;color:#333;margin-left:10px">&rdquo;</span></p>
</section>

<section class="abs gallery">
  <h2 class="section-title">Our Gallery</h2>
  <div class="abs gallery-nav">
    <span><svg width="8" height="8" viewBox="0 0 8 8"><path d="M6 0 1 4l5 4z" fill="#fff"/></svg></span>
    <span><svg width="8" height="8" viewBox="0 0 8 8"><path d="M2 0l5 4-5 4z" fill="#fff"/></svg></span>
  </div>
  <div class="abs gallery-item" style="left:97px;background:linear-gradient(180deg,#eeece8 0%,#e6e2de 40%,#f5f4f2 65%,#c9c4c0 100%)" role="img" aria-label="Older woman resting on a sofa"></div>
  <div class="abs gallery-item" style="left:343px;background:linear-gradient(90deg,#b79a86 0%,#2c2a35 25%,#d7b196 50%,#3a2f4a 75%,#1f1d2a 100%)" role="img" aria-label="Women exercising in a gym class"></div>
  <div class="abs gallery-item" style="left:592px;background:linear-gradient(90deg,#f4ece8 0%,#e9a9b4 30%,#f2e6e2 55%,#c98a8e 80%,#efe3e0 100%)" role="img" aria-label="Nurse checking a patient's blood pressure"></div>
  <div class="abs gallery-item" style="left:839px;background:linear-gradient(90deg,#cbb29a 0%,#e7d9c8 30%,#f0d9a8 55%,#f6f1ea 80%,#d9c5ae 100%)" role="img" aria-label="Woman enjoying a healthy meal"></div>
</section>

<footer class="abs site-footer">
  <h4 class="abs footer-title" style="left:97px;top:36px">Our Address</h4>
  <div class="abs" style="left:97px;top:72px">
    <p class="footer-line"><svg width="11" height="14" viewBox="0 0 11 14" style="margin-top:4px"><path d="M5.5 0A5.5 5.5 0 0 0 0 5.5C0 9 5.5 14 5.5 14S11 9 11 5.5A5.5 5.5 0 0 0 5.5 0zm0 8a2.5 2.5 0 1 1 0-5 2.5 2.5 0 0 1 0 5z" fill="#fff"/></svg><span>2750 Willow Court, Suite 4<br>Fernvale, CA 90000<br>Monday - Friday 8am - 5pm</span></p>
  </div>
  <div class="abs" style="left:370px;top:72px">
    <p class="footer-line"><svg width="13" height="13" viewBox="0 0 13 13" style="margin-top:4px"><rect width="13" height="13" rx="2" fill="#fff"/><path d="M4 3l1.5 2-1 1q1 2 3 3l1-1 2 1.5-1 1.5Q5 10 3 4z" fill="#252525"/></svg>1800 555 0142</p>
    <p class="footer-line" style="margin-top:10px"><svg width="13" height="11" viewBox="0 0 13 11" style="margin-top:5px"><rect x=".5" y=".5" width="12" height="10" fill="none" stroke="#fff"/><path d="M.5.5l6 5 6-5" fill="none" stroke="#fff"/></svg>info@meridianclinic.example</p>
  </div>
  <h4 class="abs footer-title" style="left:906px;top:48px;font-size:17px">Connect Us:</h4>
  <div class="abs social" style="left:906px;top:90px" aria-label="Social media links"><span></span><span></span><span></span><span></span></div>
  <p class="abs copyright" style="top:199px">Copyright &copy; 2015 <b>Women's health clinic</b> All Right Reserved</p>
</footer>

</body>
</html>
```